Velvet Soiree! Event planners need a poster for a party for Professional Latin Americans in NYC!

We want to promote a party and attract as many people as possible but from a very specific crowd.
Latin Americans that are beautiful, successful and want to enjoy an upscale night in the City with other top notch Latinos.

There are several Latin parties out there but we want to differentiate ourselves by catering to the VIP crowd. So we are looking for a very elegant, classy but sexy poster to promote our party.

We would like the black and gold tones and green. This is our web page: www.brivelanyc.com So similar tones, but you have freedom also if you want to add other colors / styles.

We want them to feel it will be a FUN party, with top notch latinos and beautiful people. Exclusive VIP feel also.

The party will be called Velvet Soiree , so would like to have an image of a moon and maybe a sexy but elegant girl leaning on it with stilletos... open to other ideas but would like to see the moon!

Reason: Extended some more days because we are getting great options and we don't know what to chose yet!! Just need some more days to review talk a bit more with the top choices and decide asap! thanks!

Target Market(s)

Beautiful, professional Latin Americans living in NYC
Above average salary , successful, sexy
Looking for a good time amongst quality people

Industry/Entity Type

Event

Requirements
Must have
• Moon
• Feel upscale and exclusive / VIP
• but keep the fun latino dancing sexy vibe
• Date: Friday 29th May at Casa Ondir NYC
Nice to have
• woman silhouette / woman next to the moon or leaning against it or sitting on it... interacting with the moon in some way

```html
<!DOCTYPE html>
<html lang="en">
<head>
<meta charset="utf-8">
<title>Velvet Soiree – Friday 29th May</title>
<link rel="stylesheet" href="https://fonts.googleapis.com/css2?family=Anton&family=Kaushan+Script&family=Open+Sans:wght@600;700&display=swap">
<style>
  :root {
    --ink: #000000;
    --night: #0b0a05;
    --gold: #c9a24a;
    --magenta: #d4226e;
    --magenta-hot: #ff2fd0;
    --magenta-deep: #7d0c3c;
    --blush: #ffe3f0;
    --white: #ffffff;
    --square-a: #3b5a9a;
    --square-b: #5fd0ef;
  }
  html, body {
    margin: 0;
    padding: 0;
    width: 849px;
    height: 1200px;
    overflow: hidden;
    background: var(--ink);
  }
  .poster {
    position: relative;
    width: 849px;
    height: 1200px;
    overflow: hidden;
    background: var(--night);
    font-family: "Open Sans", Arial, sans-serif;
    color: var(--white);
  }
  .poster-art {
    position: absolute;
    inset: 0;
  }
  .header-band {
    position: absolute;
    left: 0; top: 0;
    width: 849px;
    height: 168px;
    background: var(--ink);
    text-align: center;
  }
  .brand-name {
    position: absolute;
    left: 0; right: 0;
    top: 14px;
    margin: 0;
    font-size: 74px;
    font-weight: 700;
    line-height: 1;
    color: var(--gold);
  }
  .presents {
    position: absolute;
    left: 0; right: 0;
    top: 118px;
    margin: 0;
    font-size: 28px;
    font-weight: 700;
    letter-spacing: 16px;
    padding-left: 16px;
    line-height: 1;
  }
  .event-title {
    position: absolute;
    left: 0; top: 0;
    margin: 0;
    width: 849px;
    height: 620px;
    font-weight: 400;
  }
  .title-main {
    position: absolute;
    left: 74px;
    top: 243px;
    font-family: "Anton", Impact, sans-serif;
    font-size: 192px;
    line-height: 1;
    letter-spacing: 9px;
    color: var(--magenta);
    text-shadow: -3px -3px 0 var(--magenta-hot), 5px 5px 0 var(--magenta-deep), 0 0 22px rgba(0,0,0,.55);
  }
  .title-script {
    position: absolute;
    left: 262px;
    top: 430px;
    font-family: "Kaushan Script", cursive;
    font-size: 168px;
    line-height: 1;
    color: var(--blush);
    transform: rotate(-17deg);
    transform-origin: left center;
    text-shadow: 4px 4px 0 var(--magenta), -2px -2px 0 var(--white), 0 0 20px rgba(212,34,110,.85);
  }
  .event-details {
    position: absolute;
    left: 0; right: 0;
    top: 908px;
    text-align: center;
    font-weight: 700;
    text-shadow: 0 2px 5px rgba(0,0,0,.9);
  }
  .event-date {
    margin: 0;
    font-size: 41px;
    line-height: 1.2;
    letter-spacing: -0.6px;
  }
  .visit-label {
    margin: 4px 0 0;
    font-size: 39px;
    line-height: 1.2;
  }
  .website {
    margin: 2px 0 0;
    font-size: 53px;
    line-height: 1.15;
    letter-spacing: -0.3px;
  }
  .social {
    position: absolute;
    top: 1110px;
    display: flex;
    align-items: center;
    gap: 16px;
    font-size: 30px;
    font-weight: 700;
    text-shadow: 0 2px 5px rgba(0,0,0,.9);
  }
  .social-page { left: 51px; }
  .social-handle { left: 345px; }
  .social-mark {
    display: block;
    width: 78px;
    height: 78px;
    border-radius: 4px;
  }
  .social-page .social-mark { background: var(--square-a); }
  .social-handle .social-mark { background: var(--square-b); border-radius: 14px; }
  .social-text { padding-top: 30px; }
</style>
</head>
<body>
<main class="poster">
  <svg class="poster-art" width="849" height="1200" viewBox="0 0 849 1200" xmlns="http://www.w3.org/2000/svg">
    <defs>
      <radialGradient id="moonFill" cx="0.42" cy="0.4" r="0.65">
        <stop offset="0" stop-color="#cfc24c"/>
        <stop offset="0.45" stop-color="#ada234"/>
        <stop offset="0.8" stop-color="#8c8328"/>
        <stop offset="1" stop-color="#5e5a1a"/>
      </radialGradient>
      <radialGradient id="moonShade" cx="0.7" cy="0.35" r="0.3">
        <stop offset="0" stop-color="#4f4a14" stop-opacity="0.45"/>
        <stop offset="1" stop-color="#4f4a14" stop-opacity="0"/>
      </radialGradient>
      <radialGradient id="moonGlow" cx="0.5" cy="0.5" r="0.5">
        <stop offset="0.78" stop-color="#f0e46a" stop-opacity="0.6"/>
        <stop offset="1" stop-color="#f0e46a" stop-opacity="0"/>
      </radialGradient>
      <radialGradient id="skyFill" cx="0.5" cy="0.35" r="0.75">
        <stop offset="0" stop-color="#3a3510"/>
        <stop offset="0.6" stop-color="#17150a"/>
        <stop offset="1" stop-color="#050402"/>
      </radialGradient>
      <linearGradient id="goldRule" x1="0" x2="0" y1="0" y2="1">
        <stop offset="0" stop-color="#e2bf63"/>
        <stop offset="1" stop-color="#7a5716"/>
      </linearGradient>
      <linearGradient id="cityFill" x1="0" x2="0" y1="0" y2="1">
        <stop offset="0" stop-color="#14120a"/>
        <stop offset="0.35" stop-color="#3a3518"/>
        <stop offset="0.75" stop-color="#6b6226"/>
        <stop offset="1" stop-color="#877b30"/>
      </linearGradient>
      <radialGradient id="cityLights" cx="0.5" cy="0.55" r="0.6">
        <stop offset="0" stop-color="#c2b14a" stop-opacity="0.35"/>
        <stop offset="1" stop-color="#c2b14a" stop-opacity="0"/>
      </radialGradient>
      <linearGradient id="cityEdge" x1="0" x2="1" y1="0" y2="0">
        <stop offset="0" stop-color="#000" stop-opacity="0.55"/>
        <stop offset="0.25" stop-color="#000" stop-opacity="0"/>
        <stop offset="0.75" stop-color="#000" stop-opacity="0"/>
        <stop offset="1" stop-color="#000" stop-opacity="0.55"/>
      </linearGradient>
      <linearGradient id="mingleBase" x1="0" x2="1" y1="0" y2="0.4">
        <stop offset="0" stop-color="#3a2c22"/>
        <stop offset="0.3" stop-color="#6d5a4c"/>
        <stop offset="0.6" stop-color="#b9b3b6"/>
        <stop offset="0.85" stop-color="#4a3a33"/>
        <stop offset="1" stop-color="#1c1814"/>
      </linearGradient>
      <radialGradient id="mingleWarm" cx="0.45" cy="0.45" r="0.4">
        <stop offset="0" stop-color="#e0b090" stop-opacity="0.6"/>
        <stop offset="1" stop-color="#e0b090" stop-opacity="0"/>
      </radialGradient>
      <radialGradient id="mingleGlow" cx="0.35" cy="0.75" r="0.3">
        <stop offset="0" stop-color="#e8c85a" stop-opacity="0.45"/>
        <stop offset="1" stop-color="#e8c85a" stop-opacity="0"/>
      </radialGradient>
      <linearGradient id="danceBase" x1="0" x2="1" y1="0" y2="1">
        <stop offset="0" stop-color="#2a1a3a"/>
        <stop offset="0.35" stop-color="#3d2a55"/>
        <stop offset="0.6" stop-color="#6a4a3a"/>
        <stop offset="1" stop-color="#1a1420"/>
      </linearGradient>
      <radialGradient id="danceBlue" cx="0.3" cy="0.2" r="0.45">
        <stop offset="0" stop-color="#5fb0ff" stop-opacity="0.6"/>
        <stop offset="1" stop-color="#5fb0ff" stop-opacity="0"/>
      </radialGradient>
      <radialGradient id="dancePink" cx="0.82" cy="0.15" r="0.35">
        <stop offset="0" stop-color="#ff4a6a" stop-opacity="0.75"/>
        <stop offset="1" stop-color="#ff4a6a" stop-opacity="0"/>
      </radialGradient>
      <radialGradient id="danceSkin" cx="0.55" cy="0.4" r="0.35">
        <stop offset="0" stop-color="#d49a78" stop-opacity="0.5"/>
        <stop offset="1" stop-color="#d49a78" stop-opacity="0"/>
      </radialGradient>
    </defs>

    <rect class="stage-bg" x="0" y="180" width="849" height="1020" fill="url(#skyFill)"/>

    <g role="img" aria-label="Full golden moon glowing in the night sky">
      <circle cx="437" cy="412" r="312" fill="url(#moonGlow)"/>
      <circle cx="437" cy="412" r="290" fill="url(#moonFill)"/>
      <circle cx="437" cy="412" r="290" fill="url(#moonShade)"/>
    </g>

    <g role="img" aria-label="Night-time city skyline seen from above, lit in gold">
      <rect x="0" y="840" width="849" height="360" fill="url(#cityFill)"/>
      <rect x="0" y="840" width="849" height="360" fill="url(#cityLights)"/>
      <rect x="0" y="840" width="849" height="360" fill="url(#cityEdge)"/>
    </g>

    <g role="img" aria-label="Photo of elegant guests mingling with champagne glasses">
      <polygon points="0,639 427,600 427,845 0,888" fill="url(#mingleBase)"/>
      <polygon points="0,639 427,600 427,845 0,888" fill="url(#mingleWarm)"/>
      <polygon points="0,639 427,600 427,845 0,888" fill="url(#mingleGlow)"/>
    </g>
    <g role="img" aria-label="Photo of women dancing under nightclub lights">
      <polygon points="427,592 849,557 849,815 427,849" fill="url(#danceBase)"/>
      <polygon points="427,592 849,557 849,815 427,849" fill="url(#danceBlue)"/>
      <polygon points="427,592 849,557 849,815 427,849" fill="url(#dancePink)"/>
      <polygon points="427,592 849,557 849,815 427,849" fill="url(#danceSkin)"/>
    </g>
    <line class="photo-seam" x1="427" y1="592" x2="427" y2="849" stroke="#0d0c05" stroke-width="3"/>

    <rect class="gold-rule" x="0" y="168" width="849" height="12" fill="url(#goldRule)"/>
  </svg>

  <header class="header-band">
    <p class="brand-name">Brivela</p>
    <p class="presents">PRESENTS</p>
  </header>

  <h1 class="event-title">
    <span class="title-main">VELVET</span>
    <span class="title-script">Soiree</span>
  </h1>

  <section class="event-details">
    <p class="event-date">Friday 29th May at Casa Ondir NYC.</p>
    <p class="visit-label">Visit us at:</p>
    <p class="website">www.brivelanyc.com</p>
  </section>

  <div class="social social-page">
    <span class="social-mark" aria-hidden="true"></span>
    <span class="social-text">Brivela NYC</span>
  </div>
  <div class="social social-handle">
    <span class="social-mark" aria-hidden="true"></span>
    <span class="social-text">@BrivelaNYC</span>
  </div>
</main>
</body>
</html>
```